Ciel doux

Hello,
I’m a designer sunglasses reatail Store owner in Montreal, Quebec.

Looking for something modern, fresh with a trendy appeal.

Will send my logo.
Thank you.

Store

```html
<!DOCTYPE html>
<html lang="fr">
<head>
<meta charset="utf-8">
<title>Ciel doux – cartes professionnelles</title>
<link rel="stylesheet" href="https://fonts.googleapis.com/css2?family=Nunito+Sans:wght@400;600;800&display=swap">
<style>
  :root {
    --backdrop: #151515;
    --card: #242424;
    --card-edge: #2b2b2b;
    --accent: #c8202f;
    --ink-light: #f2f2f2;
    --ink-emboss: #1c1c1c;
  }
  * { box-sizing: border-box; margin: 0; padding: 0; }
  html, body {
    width: 1200px; height: 900px; overflow: hidden;
    background: var(--backdrop);
    font-family: "Nunito Sans", sans-serif;
  }
  .stage {
    position: relative; width: 1200px; height: 900px;
    display: flex; flex-direction: column; align-items: center; justify-content: center; gap: 50px;
  }
  .card {
    position: relative; width: 700px; height: 390px;
    background: linear-gradient(135deg, var(--card-edge), var(--card));
    border-bottom: 12px solid var(--accent);
    overflow: hidden;
  }
  .card--front { display: flex; align-items: center; justify-content: center; }
  .brand-emboss {
    display: flex; align-items: center; gap: 22px;
    font-weight: 800; font-size: 64px; letter-spacing: 6px; text-transform: uppercase;
    color: var(--ink-emboss);
  }
  .brand-emboss .brand-dot {
    width: 70px; height: 70px; border-radius: 50%; background: var(--ink-emboss);
  }
  .card--back { display: flex; align-items: center; padding: 0 50px 0 60px; }
  .brand-small {
    flex: 0 0 260px; display: flex; align-items: center; gap: 14px;
    font-weight: 800; font-size: 32px; letter-spacing: 3px; text-transform: uppercase;
    color: var(--ink-light); white-space: nowrap;
  }
  .brand-small .brand-dot {
    width: 36px; height: 36px; border-radius: 50%; background: var(--accent); flex: none;
  }
  .divider { width: 2px; height: 170px; background: var(--accent); margin: 0 38px 0 14px; flex: none; }
  .contact { color: var(--ink-light); white-space: nowrap; }
  .contact__name {
    font-weight: 800; font-size: 33px; letter-spacing: 2px; text-transform: uppercase;
    color: var(--accent); line-height: 1;
  }
  .contact__role { font-size: 22px; font-weight: 600; margin: 4px 0 20px; }
  .contact__list { list-style: none; }
  .contact__item {
    display: flex; align-items: center; gap: 14px;
    font-size: 19px; letter-spacing: 1px; line-height: 1.55;
  }
  .contact__icon { width: 15px; height: 15px; flex: none; fill: var(--accent); }
</style>
</head>
<body>
<main class="stage">
  <section class="card card--front" aria-label="Recto de la carte">
    <div class="brand-emboss"><span class="brand-dot"></span>Ciel doux</div>
  </section>

  <section class="card card--back" aria-label="Verso de la carte">
    <div class="brand-small"><span class="brand-dot"></span>Ciel doux</div>
    <div class="divider"></div>
    <div class="contact">
      <p class="contact__name">Noé Valtier</p>
      <p class="contact__role">Founder/CEO</p>
      <ul class="contact__list">
        <li class="contact__item">
          <svg class="contact__icon" viewBox="0 0 16 16" aria-hidden="true"><path d="M3.5 1 6 3.5 4.7 5.4a8 8 0 0 0 5.9 5.9L12.5 10 15 12.5 13 14.8C7 14.8 1.2 9 1.2 3z"/></svg>
          555.010.2244
        </li>
        <li class="contact__item">
          <svg class="contact__icon" viewBox="0 0 16 16" aria-hidden="true"><path d="M1 3h14v10H1z M1 3l7 6 7-6" fill="var(--accent)" stroke="var(--card)" stroke-width="1"/></svg>
          noe@cieldoux.com
        </li>
        <li class="contact__item">
          <svg class="contact__icon" viewBox="0 0 16 16" aria-hidden="true"><circle cx="8" cy="8" r="7"/><path d="M1 8h14M8 1c3 3 3 11 0 14M8 1c-3 3-3 11 0 14" fill="none" stroke="var(--card)" stroke-width="1"/></svg>
          cieldouxlunettes.com
        </li>
      </ul>
    </div>
  </section>
</main>
</body>
</html>
```